"Tidewell Kids" needs a A5 flyer for its "Art Contest"

Tidewell Kids needs a double sided A5 Flyer that illustrates in a child-friendly look the following competition:

Search for the up and coming Sprout Sketcher. The aim of our Sprout Sketcher is to allow our children to explore the artist within them and motivate them to express their talents through the fine art of drawing and painting.

Description: I have an art school, "Tidewell Kids", where children of 3-5 years old attend and learn how to paint and draw. We are making a competition where each child gets to draw a picture which we will upload to Friendloop and parents will vote for best picture. We need to distribute to the parents a flyer with following content.

Competition Name: Sprout Sketcher

Front Side (content):
No major text on the front. Only the Logo and messages grabbing the readers attention such as "Who will be our next Artist?", "Vote for your Child", "Like Us on our Friendloop Page".

Back Side (content):
Back side content is divided into 3 sections:

Section1:
How it Works?
Every child of every class will participate. Photos will be grouped by class.
There will be a Sprout Sketcher for each class, and there will be a Sprout Sketcher for the school.

Section2:
How to Participate?
In our search for ‘Sprout Sketcher’, we will select one piece of artwork from each child in the school, photograph it and upload it to our Friendloop page.
Vote for your favourite painting by following the steps below:
1- From your friendloop account go to www.friendloop-kids.net/Tidewell Kids
and “Like Us” to become a fan
2- Click on the“Sprout Sketcher” from the application menu
3- Browse through the different classes and vote for each picture you like
4- Invite your friends to vote for the picture you like to increase the chances of winning
The artist of the painting with most “Likes” will be crowned ‘Sprout Sketcher’.

Section3:
Note (in the footer):
Please note that the winner’s photo will be displayed in our “Sprout Sketcher” Frame on our Friendloop landing page. If you do not want your child’s photograph to be posted on our Friendloop page in this manner, please let us know by sending an e-mail.
, Tidewell Kids needs a double sided A5 Flyer that illustrates in a child-friendly look the following competition:

Front Side (content):

Back Side (content):

Section1:
How it Works?

Section2:
How to Participate?

Section3:
Note (in the footer):

Parents of the children attending at our school, Parents of the children attending at our school

Painting

• Colors used in the design should be strict to our logo colors. We have 4 colors in our logo feel free to use one or all of them through out the design:
#6CB53C
#DB2718
#5D9DD5
#F4D602

The elements in our logo are playful and hand drawn and written, so the flyer design should reflect the hand made style rather than solid elements and objects., Colors used in the design should be strict to our logo colors. We have 4 colors in our logo feel free to use one or all of them through out the design:
#6CB53C
#DB2718
#5D9DD5
#F4D602

The elements in our logo are playful and hand drawn and written, so the flyer design should reflect the hand made style rather than solid elements and objects.
• Images of real children., Images of real children.

```html
<!DOCTYPE html>
<html lang="en">
<head>
<meta charset="utf-8">
<title>Sprout Sketcher – Tidewell Kids</title>
<link href="https://fonts.googleapis.com/css2?family=Fredoka:wght@600&family=Chewy&family=Arimo:wght@700&display=swap" rel="stylesheet">
<style>
  :root {
    --green: #6CB53C;
    --lime: #9CC63B;
    --red: #DB2718;
    --blue: #5D9DD5;
    --deep-blue: #2F7FC7;
    --yellow: #F4D602;
    --orange: #F7B84B;
    --purple: #7B4FB0;
    --teal: #4DB89A;
    --white: #FFFFFF;
  }
  * { margin: 0; padding: 0; box-sizing: border-box; }
  html, body { width: 845px; height: 1200px; overflow: hidden; background: var(--white); }
  .flyer { position: relative; width: 845px; height: 1200px; overflow: hidden; background: var(--white); }

  .paint-drips {
    position: absolute; left: 0; top: 0; width: 845px; height: 250px;
    background: linear-gradient(90deg, var(--green) 0%, var(--red) 30%, var(--yellow) 50%, var(--blue) 72%, var(--purple) 100%);
    border-radius: 0 0 60px 60px;
    opacity: 0.9;
  }

  .title {
    position: absolute; left: 0; top: 52px; width: 845px; text-align: center;
    font-family: "Fredoka", sans-serif; font-weight: 600; font-size: 74px;
    letter-spacing: 1px; line-height: 1;
    -webkit-text-stroke: 6px var(--white); paint-order: stroke fill;
  }
  .title .c1 { color: var(--blue); }
  .title .c2 { color: var(--red); }
  .title .c3 { color: var(--yellow); }
  .title .c4 { color: var(--green); }
  .title .c5 { color: var(--purple); }

  .photo-frame {
    position: absolute; left: 100px; top: 172px; width: 500px; height: 410px;
    background: var(--yellow); padding: 16px; transform: rotate(-4deg);
  }
  .photo {
    width: 100%; height: 100%;
    background: linear-gradient(135deg, #F4E7D8 0%, #E8C7A8 45%, #9CC7E8 80%, #F1F1F1 100%);
  }

  .banners { position: absolute; left: 0; top: 0; }

  .headline {
    position: absolute; left: 70px; top: 672px;
    font-family: "Chewy", cursive; color: var(--yellow); line-height: 1;
  }
  .headline .lead { display: block; font-size: 46px; letter-spacing: 2px; }
  .headline .main { display: block; font-size: 80px; letter-spacing: 3px; margin-top: 8px; }

  .vote {
    position: absolute; left: 380px; top: 876px; width: 430px;
    font-family: "Arimo", sans-serif; font-weight: 700; font-size: 40px; color: var(--white);
  }
  .like {
    position: absolute; left: 38px; top: 980px; width: 360px; text-align: center;
    font-family: "Arimo", sans-serif; font-weight: 700; font-size: 27px; line-height: 1.3; color: var(--white);
  }
  .join {
    position: absolute; left: 40px; top: 1096px; width: 330px; text-align: center;
    font-family: "Chewy", cursive; font-size: 46px; letter-spacing: 2px; color: var(--white);
    -webkit-text-stroke: 2px #2E7A63; paint-order: stroke fill;
  }

  .brand {
    position: absolute; left: 470px; top: 1050px; display: flex; align-items: center; gap: 14px;
  }
  .brand-dot { width: 36px; height: 36px; border-radius: 50%; background: var(--green); }
  .brand-name {
    font-family: "Fredoka", sans-serif; font-weight: 600; font-size: 50px; color: var(--red);
  }
</style>
</head>
<body>
<main class="flyer">
  <div class="paint-drips" role="img" aria-label="Colourful paint dripping down from the top edge in green, red, yellow, blue and purple"></div>

  <h1 class="title"><span class="c1">S</span><span class="c2">P</span><span class="c3">R</span><span class="c4">O</span><span class="c1">U</span><span class="c2">T</span> <span class="c5">S</span><span class="c4">K</span><span class="c3">E</span><span class="c1">T</span><span class="c2">C</span><span class="c4">H</span><span class="c5">E</span><span class="c1">R</span></h1>

  <div class="photo-frame">
    <div class="photo" role="img" aria-label="Photo of a young child with paint-covered hands raised beside his head"></div>
  </div>

  <svg class="banners" width="845" height="1200" viewBox="0 0 845 1200" aria-hidden="true">
    <path d="M40 640 Q 300 612 560 628 Q 720 620 845 612 L 845 948 Q 600 962 380 944 Q 200 954 60 940 Q 30 800 40 640 Z" fill="var(--deep-blue)"/>
    <path d="M350 866 Q 560 852 800 860 Q 826 896 806 936 Q 580 946 360 938 Q 336 902 350 866 Z" fill="var(--lime)"/>
    <path d="M0 962 Q 200 950 400 960 Q 418 1020 392 1082 Q 200 1090 0 1080 Z" fill="var(--orange)"/>
    <path d="M0 1078 Q 200 1068 372 1076 Q 392 1120 370 1164 Q 200 1172 0 1160 Z" fill="var(--teal)"/>
  </svg>

  <h2 class="headline"><span class="lead">WHO WILL BE OUR</span><span class="main">NEXT ARTIST?</span></h2>
  <p class="vote">Vote for your Child</p>
  <p class="like">Like Us on our<br>Friendloop Page</p>
  <p class="join">JOIN NOW</p>

  <div class="brand">
    <span class="brand-dot"></span>
    <span class="brand-name">Tidewell Kids</span>
  </div>
</main>
</body>
</html>
```